Sparkling Wine Label Wren Hollow

Super Premium Sparkling Wine Label

We are a super premium tasmanian fine wine producer and are about to release our first Sparking Wine.

please visit www.wrenhollowvines.com.au to check out our range of wine. We need a label that will sit within this branding but as the aspirational product. We think that the Mavet grey/navy label will fit into this concept. It is masculine clean elegent and very smick,
and would be a great addition to our line see Copper Pinot Noir label.

However you can be quite creative with Sparkling Line eg Tollis Prime Reserve is a stunning classical french label featuring gold baroque detail and feminine elegence.

Its up to you if you where spending $50 on a special bottles of sparkling wine what would you expect to see?

Black/Gold Graphite/Gold

Needs a neck /collar label

Main Front Label
Wren Hollow
Chardonnay Pinot Noir
Tasmania

Back label has all the techical into you can use the back label from existing labels but reverserve out the colours to black and white or graphite and white

We want a label that oozes quality and expense. That says this the way I want to celebrate.

Target Market(s)

40 60 age group appreciator of quality

Industry/Entity Type

Product

Requirements
Must have
• Neck label
Simular to Mavet Shield so
WREN arched above
G rondel in middle possibiliy replacing coat of arms
TASMANIA arched under in red

Main Front Label
Wren Hollow
Tasmania
Chardonnay Pinot Noir 750ML

Back Label / use the attachment Wren label just reverse out so that it is a black label with white writing and amend information
Wren Hollow
23 Ferny Marsh Rd Dunleigh
Tasmania, 7190
0417293856
www.wrenhollowvines.com.au
contact@wrenhollowvines.com.au
Sulphur Dioxide Added
Alc/Vol 12.5%
7.7 Standard Drinks

Rondel g
Nice to have

```html
<!DOCTYPE html>
<html lang="en">
<head>
<meta charset="utf-8">
<title>Wren Hollow – Sparkling Labels</title>
<link rel="stylesheet" href="https://fonts.googleapis.com/css2?family=Cormorant+Garamond:wght@500&family=Tinos&family=Open+Sans:wght@300;400&display=swap">
<style>
  :root {
    --bg-light: #f4f4f5;
    --bg-dark: #c9c9cc;
    --lavender: #a7a8e6;
    --lavender-deep: #6c6aa6;
    --lavender-rim: #b9baf0;
    --wine-red: #6a0f1e;
    --silver-light: #d6d7da;
    --silver-dark: #b3b4b8;
    --frame-grey: #8e8f94;
    --ink: #2b2b2e;
    --ink-soft: #8d8e93;
    --stripe: #8f90c9;
  }
  * { margin: 0; padding: 0; box-sizing: border-box; }
  html, body { width: 1200px; height: 1000px; overflow: hidden; }
  body {
    position: relative;
    background: radial-gradient(ellipse at 70% 30%, var(--bg-light), var(--bg-dark));
  }

  /* Neck collar */
  .neck-label { position: absolute; left: 250px; top: 50px; width: 700px; height: 360px; }
  .neck-label svg { display: block; }
  .neck-brand { font-family: "Cormorant Garamond", serif; font-size: 78px; fill: var(--wine-red); }
  .neck-origin { font-family: "Tinos", serif; font-size: 22px; fill: var(--wine-red); }

  /* Front label */
  .front-label {
    position: absolute; left: 280px; top: 450px; width: 640px; height: 470px;
    background: linear-gradient(100deg, var(--silver-dark), var(--silver-light) 45%, var(--silver-dark));
  }
  .front-frame {
    position: absolute; inset: 14px 14px 20px 14px;
    border: 1px solid var(--frame-grey);
  }
  .side-stripe {
    position: absolute; left: 92px; top: 14px; bottom: 20px; width: 9px;
    background: linear-gradient(90deg, var(--stripe), var(--lavender-rim));
  }
  .side-story {
    position: absolute; left: 52px; top: 250px; width: 300px;
    transform: translate(-50%, -50%) rotate(-90deg);
    transform-origin: center;
    font-family: "Tinos", serif; font-size: 11px; line-height: 13px;
    color: var(--ink);
    margin-left: 0;
  }
  .side-story p { width: 300px; }
  .brand-name {
    position: absolute; left: 170px; top: 130px;
    font-family: "Cormorant Garamond", serif; font-weight: 500;
    font-size: 140px; line-height: 1; color: var(--ink);
  }
  .brand-sub {
    position: absolute; left: 262px; top: 275px;
    font-family: "Open Sans", sans-serif; font-weight: 300;
    font-size: 22px; letter-spacing: 2px; color: var(--ink-soft);
  }
  .vintage {
    position: absolute; left: 262px; top: 318px;
    font-family: "Open Sans", sans-serif; font-size: 19px; line-height: 24px; color: var(--ink);
  }
  .volume {
    position: absolute; left: 30px; top: 404px;
    font-family: "Open Sans", sans-serif; font-size: 19px; color: var(--ink);
  }
  .origin {
    position: absolute; left: 262px; top: 408px;
    font-family: "Tinos", serif; font-size: 15px; color: var(--ink);
  }
</style>
</head>
<body>

<section class="neck-label" aria-label="Neck collar label">
  <svg width="700" height="360" viewBox="0 0 700 360">
    <defs>
      <linearGradient id="collarBand" x1="0" y1="0" x2="1" y2="0">
        <stop offset="0" stop-color="#8d8fd6"/>
        <stop offset="0.5" stop-color="#b4b5ee"/>
        <stop offset="1" stop-color="#8d8fd6"/>
      </linearGradient>
    </defs>
    <rect class="collar-band" x="0" y="125" width="700" height="110" fill="url(#collarBand)"/>
    <circle class="roundel-rim" cx="350" cy="180" r="172" fill="var(--lavender-rim)"/>
    <circle class="roundel-face" cx="350" cy="180" r="162" fill="var(--lavender-deep)"/>
    <text class="neck-brand" x="350" y="95" text-anchor="middle">Wren</text>
    <circle class="roundel-ring" cx="350" cy="190" r="72" fill="none" stroke="#d9dae0" stroke-width="2"/>
    <text class="neck-origin" x="350" y="312" text-anchor="middle">Dunleigh Tasmania</text>
  </svg>
</section>

<section class="front-label" aria-label="Front label">
  <div class="front-frame"></div>
  <div class="side-stripe"></div>
  <div class="side-story">
    <p>Grown on cool slopes near the river flats of Dunleigh, our vines</p>
    <p>ripen slowly under long summer light, giving fine bubbles</p>
    <p>and a crisp, layered finish worth a celebration.</p>
  </div>
  <div class="brand-name">Wren</div>
  <div class="brand-sub">HOLLOW</div>
  <div class="vintage">2013<br>Chardonnay Pinot Noir</div>
  <div class="volume">750 ml</div>
  <div class="origin">Dunleigh Tasmania</div>
</section>

</body>
</html>
```